Valorix is a financial services company which transacts by allowing clients to purchase Brimtoken (c

I need a lumo themed site (if possible) but I can work with html as well since I have paid for the CSS very simple that will simply show what valorix is and what we graphically need to do in order to make the transaction happen

Target Market(s)

Any persons over the age of 18 globally who wants to purchase Brimtoken (crypto currency) with their credit cards and receive a brim wallet from Valorix

Industry/Entity Type

Insurance

Coding

Coded - Design and coding required

Number of Pages Required

3 page

Font styles to use
Serif

Colors
3277b5
3176b5
85acd3
85cae6

Requirements
Must have
• Logo visible top let on all pages ... color scheme that evokes trust, confidence, transparency.. terms and conditions and privacy policy footer links
Nice to have
• I willl have logo chosen in next 24 hrs..

```html
<!DOCTYPE html>
<html lang="en">
<head>
<meta charset="utf-8">
<title>Valorix — Credit Card to Brimtoken</title>
<link href="https://fonts.googleapis.com/css2?family=Playfair+Display:wght@700;800&family=PT+Serif:wght@400;700&display=swap" rel="stylesheet">
<style>
:root{
  --brand:#3277b5;
  --brand-alt:#3176b5;
  --soft:#85acd3;
  --sky:#85cae6;
  --deep:#2a649d;
  --ink:#333a44;
  --muted:#5b6470;
  --white:#ffffff;
  --star:#f5b81c;
  --red:#e03a2f;
  --head:"Playfair Display",Georgia,serif;
  --body:"PT Serif",Georgia,serif;
}
*{margin:0;padding:0;box-sizing:border-box}
html,body{width:1200px;height:3297px;overflow:hidden}
body{font-family:var(--body);color:var(--ink);background:var(--white);position:relative}
.section{position:absolute;left:0;width:1200px;overflow:hidden}
.abs{position:absolute}
.heading{font-family:var(--head);font-weight:700;color:var(--brand);text-align:center;width:1200px;left:0;font-size:40px;letter-spacing:.5px}
.btn{position:absolute;display:flex;align-items:center;justify-content:center;background:var(--sky);color:var(--white);font-family:var(--head);font-weight:700;font-size:20px;letter-spacing:.5px;border-radius:6px;box-shadow:0 3px 6px rgba(0,0,0,.15)}

/* top bar */
.topbar{top:0;height:42px;background:var(--brand)}
.social-sq{position:absolute;top:0;width:42px;height:42px;border-right:1px solid rgba(255,255,255,.3)}
.social-sq span{position:absolute;left:14px;top:14px;width:14px;height:14px;border-radius:50%;background:var(--white)}
.callus{position:absolute;right:76px;top:7px;color:var(--white);font-size:15px;display:flex;align-items:center;gap:12px}
.callus .num{font-weight:700;font-size:17px}
.callus .phone{width:30px;height:30px;border-radius:50%;background:var(--white);display:flex;align-items:center;justify-content:center}

/* hero */
.hero{top:42px;height:635px;background:linear-gradient(100deg,#d7e2ec 0%,#9fb5c9 30%,#44586e 55%,#2c3c50 75%,#7e95ae 100%)}
.hero-photo{position:absolute;inset:0}
.site-header{position:absolute;top:0;left:0;width:1200px;height:83px;background:rgba(255,255,255,.85)}
.logo{position:absolute;left:77px;top:12px;font-family:var(--head);font-weight:800;font-size:44px;color:var(--brand)}
.nav{position:absolute;right:60px;top:22px;display:flex;gap:26px;align-items:center;font-family:var(--body);font-weight:400;font-size:15.5px;color:#222}
.nav .search{width:38px;height:38px;border-radius:50%;background:var(--brand);display:flex;align-items:center;justify-content:center}
.hero-title{position:absolute;left:77px;top:232px;font-family:var(--head);font-weight:800;font-size:38px;line-height:48px;color:var(--brand);text-transform:uppercase}
.hero-sub{position:absolute;left:77px;top:340px;font-weight:700;font-size:19px;color:#111}
.arrow{position:absolute;top:324px;width:50px;height:50px;border-radius:50%;background:var(--brand);display:flex;align-items:center;justify-content:center}

/* welcome */
.welcome{top:677px;height:376px;background:linear-gradient(100deg,var(--brand) 0%,#4a8cc6 50%,var(--sky) 100%)}
.welcome .heading{color:var(--white);top:60px;font-size:40px}
.welcome p{position:absolute;left:150px;width:900px;top:126px;font-size:13px;line-height:24px;color:var(--white);text-align:center}

/* services */
.services{top:1053px;height:470px;background:var(--white)}
.service{position:absolute;top:147px;width:250px;text-align:center}
.service .icon{margin:0 auto;width:114px;height:114px;border-radius:50%;background:var(--brand);display:flex;align-items:center;justify-content:center}
.service .icon.light{background:var(--sky)}
.service h3{margin-top:26px;font-family:var(--body);font-weight:700;font-size:16px;line-height:25px;color:var(--brand)}
.service p{margin-top:14px;font-size:13px;line-height:23px;color:var(--ink)}

/* why */
.why{top:1523px;height:519px;background:linear-gradient(100deg,#3a79b6 0%,#5c93c7 45%,#3d7ab5 100%)}
.why h2{position:absolute;left:79px;top:52px;font-family:var(--head);font-weight:700;font-size:40px;color:var(--white)}
.checklist{position:absolute;left:79px;top:137px;list-style:none}
.checklist li{display:flex;align-items:center;gap:18px;height:47px;color:var(--white);font-size:17px}
.video{position:absolute;left:602px;top:77px;width:519px;height:363px;border:4px solid var(--sky);background:linear-gradient(120deg,#c9d6e2 0%,#8ea5bb 40%,#e7edf3 70%,#7a9ab9 100%)}
.play{position:absolute;left:222px;top:145px;width:68px;height:68px;border-radius:50%;background:var(--red);display:flex;align-items:center;justify-content:center}

/* testimonials */
.testimonials{top:2042px;height:475px;background:var(--white)}
.testimonials .heading{top:62px}
.quote{position:absolute;top:149px;width:518px;height:159px;background:var(--white);box-shadow:0 2px 10px rgba(0,0,0,.15);padding:34px 56px;font-size:13px;line-height:26px;text-align:center}
.quote.faded{opacity:.35}
.quote .mark{position:absolute;font-family:var(--head);font-size:40px;color:var(--sky);line-height:1}
.quote::after{content:"";position:absolute;left:60px;bottom:-14px;width:26px;height:26px;background:var(--white);transform:rotate(45deg);box-shadow:3px 3px 5px rgba(0,0,0,.08)}
.person{position:absolute;top:336px;display:flex;align-items:center;gap:18px}
.person.faded{opacity:.4}
.avatar{width:78px;height:78px;border-radius:50%;background:linear-gradient(135deg,#f2e3cf,#d8b996);border:3px solid var(--white);box-shadow:0 2px 6px rgba(0,0,0,.25)}
.person .name{font-family:var(--body);font-weight:700;font-size:19px;color:var(--brand)}
.stars{display:flex;gap:3px;margin-top:6px}

/* contact */
.contact{top:2517px;height:468px;background:linear-gradient(100deg,#e7edf2 0%,#d4dde5 40%,#c1ccd7 70%,#dfe6ec 100%)}
.contact .heading{top:56px}
.contact .lead{position:absolute;left:240px;width:720px;top:120px;text-align:center;font-size:15px;line-height:26px;color:#333}
.field{position:absolute;height:50px;width:347px;background:rgba(255,255,255,.88);border:1px solid #d6dde4;font-size:13px;color:#666;padding:15px 14px}

/* footer */
.footer{top:2985px;height:253px;background:var(--brand);color:var(--white)}
.footer .flogo{position:absolute;left:77px;top:82px;font-family:var(--head);font-weight:800;font-size:42px;color:var(--white)}
.fsocial{position:absolute;left:110px;top:147px;display:flex;gap:8px}
.fsocial span{width:40px;height:40px;border-radius:50%;border:2px solid var(--white)}
.fsocial span.on{background:var(--white)}
.fcol{position:absolute;top:34px}
.fcol h4{font-family:var(--body);font-weight:700;font-size:17px;margin-bottom:20px}
.sitemap li{list-style:none;font-size:13px;line-height:28px;padding-left:18px;position:relative}
.sitemap li::before{content:"";position:absolute;left:2px;top:12px;width:5px;height:5px;border-radius:50%;background:var(--white)}
.finfo{display:flex;gap:14px;font-size:13px;line-height:20px;margin-bottom:16px}
.newsletter p{font-size:13px;line-height:24px;width:240px}
.subscribe{margin-top:16px;display:flex;width:250px;height:51px}
.subscribe .input{flex:1;background:var(--white);color:#333;font-size:13px;padding:17px 12px}
.subscribe .go{width:52px;background:var(--sky);display:flex;align-items:center;justify-content:center}
.copyright{top:3238px;height:59px;background:var(--deep);color:var(--white);font-size:13px;display:flex;align-items:center;justify-content:center;gap:14px}
.copyright a{color:var(--white);text-decoration:none}
.copyright .sep{opacity:.6}
</style>
</head>
<body>

<div class="section topbar">
  <div class="social-sq" style="left:77px;border-left:1px solid rgba(255,255,255,.3)"><span></span></div>
  <div class="social-sq" style="left:119px"><span></span></div>
  <div class="social-sq" style="left:161px"><span></span></div>
  <div class="callus">Call Us Today :
    <span class="phone"><svg width="16" height="16" viewBox="0 0 24 24"><path fill="#3277b5" d="M6.6 10.8a15 15 0 0 0 6.6 6.6l2.2-2.2c.3-.3.7-.4 1-.2 1.1.4 2.3.6 3.6.6.6 0 1 .4 1 1V20c0 .6-.4 1-1 1A17 17 0 0 1 3 4c0-.6.4-1 1-1h3.5c.6 0 1 .4 1 1 0 1.3.2 2.5.6 3.6.1.3 0 .7-.2 1z"/></svg></span>
    <span class="num">123 456 7890</span></div>
</div>

<section class="section hero">
  <div class="hero-photo" role="img" aria-label="Photo of business people reviewing documents and a tablet at a desk"></div>
  <header class="site-header">
    <div class="logo">Valorix</div>
    <nav class="nav"><span>HOME</span><span>ABOUT US</span><span>FAQ</span><span>SUPPORT</span><span>CONTACT US</span>
      <span class="search"><svg width="16" height="16" viewBox="0 0 20 20"><circle cx="8" cy="8" r="6" fill="none" stroke="#fff" stroke-width="2.5"/><path d="M12.5 12.5 18 18" stroke="#fff" stroke-width="2.5"/></svg></span></nav>
  </header>
  <h1 class="hero-title">Credit card to<br>Brimtoken in seconds</h1>
  <div class="hero-sub">Simple, Trusted, Low Fee Digital Money Platform</div>
  <div class="btn" style="left:77px;top:387px;width:209px;height:55px">CONTACT US</div>
  <div class="arrow" style="left:12px"><svg width="14" height="22" viewBox="0 0 14 22"><path d="M11 2 3 11l8 9" fill="none" stroke="#fff" stroke-width="2.5"/></svg></div>
  <div class="arrow" style="left:1136px"><svg width="14" height="22" viewBox="0 0 14 22"><path d="M3 2l8 9-8 9" fill="none" stroke="#fff" stroke-width="2.5"/></svg></div>
</section>

<section class="section welcome">
  <h2 class="heading abs">WELCOME TO VALORIX</h2>
  <p>Lorem Ipsum is simply dummy text of the printing and typesetting industry. Lorem Ipsum has been the industry's standard dummy text ever since the 1500s, when an unknown printer took a galley of type and scrambled it to make a type specimen book. It has survived not only five centuries, but also the leap into electronic typesetting, remaining essentially unchanged. It was popularised in the 1960s with the release of Letraset sheets containing Lorem Ipsum passages, and more recently.</p>
  <div class="btn" style="left:497px;top:255px;width:206px;height:57px">LEARN MORE</div>
</section>

<section class="section services">
  <h2 class="heading abs" style="top:54px">WHAT WE DO</h2>
  <div class="service" style="left:68px">
    <div class="icon light"><svg width="64" height="64" viewBox="0 0 64 64" fill="none" stroke="#fff" stroke-width="3"><circle cx="26" cy="36" r="14"/><circle cx="40" cy="26" r="12"/><path d="M8 20a24 24 0 0 1 20-14M56 44a24 24 0 0 1-20 14"/><path d="M24 4l4 2-2 4M40 60l-4-2 2-4"/></svg></div>
    <h3>instantely exchange<br>your dollars for brimtoken</h3>
    <p>Lorem Ipsum is simply dummy text of the printing and typesetting industry. Lorem Ipsum has been.</p>
  </div>
  <div class="service" style="left:345px">
    <div class="icon"><svg width="60" height="60" viewBox="0 0 60 60" fill="none" stroke="#fff" stroke-width="3"><rect x="12" y="10" width="30" height="40" rx="2"/><path d="M20 6h14v8H20zM18 22h18M18 30h18M18 38h10M44 26l8 8-14 14-8 2 2-8z"/></svg></div>
    <h3>Real time refunds receipt, you<br>get your own digital wallet</h3>
    <p>Lorem Ipsum is simply dummy text of the printing and typesetting industry. Lorem Ipsum has been.</p>
  </div>
  <div class="service" style="left:609px">
    <div class="icon"><svg width="62" height="62" viewBox="0 0 62 62" fill="none" stroke="#fff" stroke-width="3"><circle cx="31" cy="31" r="24"/><ellipse cx="31" cy="31" rx="11" ry="24"/><path d="M7 31h48M10 19h42M10 43h42M31 7v48"/></svg></div>
    <h3>Global freedom to push Brim<br>to whereever you want.</h3>
    <p>Lorem Ipsum is simply dummy text of the printing and typesetting industry. Lorem Ipsum has been.</p>
  </div>
  <div class="service" style="left:873px">
    <div class="icon"><svg width="60" height="60" viewBox="0 0 60 60" fill="none" stroke="#fff" stroke-width="3"><path d="M24 34V12a4 4 0 0 1 8 0v16l12 3a5 5 0 0 1 4 6l-3 15H26l-10-13a4 4 0 0 1 6-5z"/><path d="M16 14a12 12 0 0 1 24 0"/></svg></div>
    <h3>Click here To Purchase<br>Brim</h3>
    <p>Lorem Ipsum is simply dummy text of the printing and typesetting industry. Lorem Ipsum has been.</p>
  </div>
</section>

<section class="section why">
  <h2>WHY BRIMTOKEN?</h2>
  <ul class="checklist">
    <li><svg width="20" height="20" viewBox="0 0 20 20"><circle cx="10" cy="10" r="9" fill="#fff"/><path d="M5.5 10l3 3 6-6" fill="none" stroke="#3277b5" stroke-width="2.2"/></svg>Easily transactable</li>
    <li><svg width="20" height="20" viewBox="0 0 20 20"><circle cx="10" cy="10" r="9" fill="#fff"/><path d="M5.5 10l3 3 6-6" fill="none" stroke="#3277b5" stroke-width="2.2"/></svg>Great upside value proposition</li>
    <li><svg width="20" height="20" viewBox="0 0 20 20"><circle cx="10" cy="10" r="9" fill="#fff"/><path d="M5.5 10l3 3 6-6" fill="none" stroke="#3277b5" stroke-width="2.2"/></svg>Super low transaction speed</li>
    <li><svg width="20" height="20" viewBox="0 0 20 20"><circle cx="10" cy="10" r="9" fill="#fff"/><path d="M5.5 10l3 3 6-6" fill="none" stroke="#3277b5" stroke-width="2.2"/></svg>Revolution tranction payout system</li>
    <li><svg width="20" height="20" viewBox="0 0 20 20"><circle cx="10" cy="10" r="9" fill="#fff"/><path d="M5.5 10l3 3 6-6" fill="none" stroke="#3277b5" stroke-width="2.2"/></svg>Master nodes</li>
  </ul>
  <div class="btn" style="left:79px;top:372px;width:207px;height:57px">CONTACT US</div>
  <div class="video" role="img" aria-label="Video still of an office desk with charts, glasses and two colleagues talking">
    <div class="play"><svg width="24" height="26" viewBox="0 0 24 26"><path d="M4 2l18 11L4 24z" fill="#fff"/></svg></div>
  </div>
</section>

<section class="section testimonials">
  <h2 class="heading abs">TESTIMONIALS</h2>
  <div class="quote faded" style="left:-227px;color:#666">Lorem Ipsum is simply dummy text of the printing and typesetting industry. Lorem Ipsum has been the industry's standard dummy text ever since the 1500s, when an unknown printer</div>
  <div class="quote" style="left:341px"><span class="mark" style="left:24px;top:22px">&#8220;</span>Lorem Ipsum is simply dummy text of the printing and typesetting industry. Lorem Ipsum has been the industry's standard dummy text ever since the 1500s, when an unknown printer<span class="mark" style="right:50px;top:104px">&#8221;</span></div>
  <div class="quote faded" style="left:906px;color:#666"><span class="mark" style="left:24px;top:22px">&#8220;</span>Lorem Ipsum is simply dummy text of the printing and typesetting industry. Lorem Ipsum has been the industry's standard dummy text ever since the 1500s, when an unknown printer</div>
  <div class="person" style="left:357px">
    <div class="avatar" role="img" aria-label="Customer portrait"></div>
    <div><div class="name">- Maren T.</div>
      <div class="stars"><svg width="130" height="22" viewBox="0 0 130 22"><g fill="#f5b81c"><path id="st" d="M11 1l3 7h7l-6 5 2 8-6-4-6 4 2-8-6-5h7z"/><use href="#st" x="27"/><use href="#st" x="54"/><use href="#st" x="81"/><use href="#st" x="108"/></g></svg></div></div>
  </div>
  <div class="person faded" style="left:928px">
    <div class="avatar" role="img" aria-label="Customer portrait"></div>
    <div><div class="name">- Maren T.</div>
      <div class="stars"><svg width="130" height="22" viewBox="0 0 130 22"><g fill="#f5b81c"><use href="#st"/><use href="#st" x="27"/><use href="#st" x="54"/><use href="#st" x="81"/><use href="#st" x="108"/></g></svg></div></div>
  </div>
  <svg class="abs" style="left:0;top:378px" width="22" height="22" viewBox="0 0 22 22"><use href="#st" fill="#f5b81c" opacity=".5"/></svg>
</section>

<section class="section contact" role="img" aria-label="Faded photo of hands typing on a keyboard">
  <h2 class="heading abs">CONTACT US</h2>
  <p class="lead">Thank you for contacting support. Due to heavy volumes please allow for 12 - 24hr responses. Use typical helpdeskly form for ur team.</p>
  <div class="field" style="left:246px;top:204px">Name *</div>
  <div class="field" style="left:605px;top:204px">Tele *</div>
  <div class="field" style="left:246px;top:268px">Email *</div>
  <div class="field" style="left:605px;top:268px">Landload *</div>
  <div class="btn" style="left:516px;top:345px;width:168px;height:57px">SUBMIT</div>
</section>

<footer class="section footer">
  <div class="flogo">Valorix</div>
  <div class="fsocial"><span class="on"></span><span></span><span></span><span></span></div>
  <div class="fcol" style="left:343px">
    <h4>SITEMAP</h4>
    <ul class="sitemap"><li>Home</li><li>About Us</li><li>Faq</li><li>Supports</li><li>Contact Us</li></ul>
  </div>
  <div class="fcol" style="left:609px">
    <h4>CONTACT US</h4>
    <div class="finfo"><svg width="16" height="22" viewBox="0 0 16 22"><path d="M8 0a8 8 0 0 1 8 8c0 6-8 14-8 14S0 14 0 8a8 8 0 0 1 8-8z" fill="#fff"/><circle cx="8" cy="8" r="3" fill="#3277b5"/></svg><span>101 - Lorem ipsum is simple<br>dummy text of print.</span></div>
    <div class="finfo"><svg width="16" height="18" viewBox="0 0 24 24"><path fill="#fff" d="M6.6 10.8a15 15 0 0 0 6.6 6.6l2.2-2.2c.3-.3.7-.4 1-.2 1.1.4 2.3.6 3.6.6.6 0 1 .4 1 1V20c0 .6-.4 1-1 1A17 17 0 0 1 3 4c0-.6.4-1 1-1h3.5c.6 0 1 .4 1 1 0 1.3.2 2.5.6 3.6.1.3 0 .7-.2 1z"/></svg><span>123 456 7890</span></div>
    <div class="finfo"><svg width="18" height="14" viewBox="0 0 18 14"><rect width="18" height="14" rx="1" fill="#fff"/><path d="M1 1l8 6 8-6" fill="none" stroke="#3277b5" stroke-width="1.5"/></svg><span>info@valorix.com</span></div>
  </div>
  <div class="fcol newsletter" style="left:873px">
    <h4>NEWSLETTER</h4>
    <p>Would you like to receive exclusive access to articles, white papers and our regular monthly newsletter?</p>
    <div class="subscribe"><div class="input">Enter Email *</div>
      <div class="go"><svg width="22" height="20" viewBox="0 0 22 20"><path d="M1 9 21 1l-4 18-6-6-3 5v-7l9-8-11 7z" fill="#fff"/></svg></div></div>
  </div>
</footer>
<div class="section copyright">
  <span>@Valorix - 2018 All Right Reserved.</span>
  <span class="sep">|</span><a href="#terms">Terms and Conditions</a>
  <span class="sep">|</span><a href="#privacy">Privacy Policy</a>
</div>

</body>
</html>
```